Book Cover Design Project

I need a book cover for a book that we will be releasing in the next few months.

It is a business book aimed at small businesses and people who want to escape the 9 - 5 and start their own business.

We want it to look similar to: http://www.tolvanbrook.example/wp-content/uploads/2010/03/fold-up.jpg and also the book designs that I have uploaded images for.

I quite like the grey / charcoal background and the bright lime green colours from the Quiet Harbor logo that I have attached. However, anything bright would be good - I am prepared to be flexible with colours. The books I have attached are a high impact as well - being bright blue with white black font with a really cool font.

The book is titled:

The Lantern Shop Plan

By Dale Vortan

Still thinking of the tagline, for now just use "Start an Online Business in no time at all"

Room for a quote/testimonial on the front of the book at the bottom, and as well on the back.

For the back cover text just use dummy text and my photo that is attached for now as well.

Barcode ISBN on the back at the bottom - price will be $19.95

Needs to be in PSD so we can change the text from our end.

I really want to get a good template made that I can edit the text for as we are still developing the book, but I want to get the book cover done so I can start advertising that it will be arriving soon.

There will probably be alterations that I need help with later down the track so looking to work with someone closely on this, and I will pay you for any extra time down the track..

Sizes will probably be around: I think 20.5cm tall and 14cm wide would be good..

Not sure how thick for the spine, it will depend on how many words get cut off, but as an estimate probably 1.5CM..
Updates

Just added some more detail to the brief.. Please read it carefully.

Target Market(s)

small business owners, professionals who want to start their own business, soon to be entrepreneurs, entrepreneurs

Industry/Entity Type

Advertising

Requirements
Must have
• The Lantern Shop Plan

and Dale Vortan must be prominent.

Tag line should be look cool under the title.

Must be very modern and cool. Needs to catch people's eyes so needs to be really punchy.

Nice to have
• Maybe a clock or stopwatch icon would be cool to add in there so it isn't just plain.. Similar to like how the books have a cool icon with them that I have attached in the uploaded images.
Should not have
• I like simplicity, artistic and very high impact. It really needs to draw you in and catch your eye.

Don't use plain boring fonts. Although I like simplicity slick design is very important - I dont want it to be boring - it has to look high quality and expensive. Therefore do not use fonts like Arial, Times New Roman those really boring fonts that make it look cheap. If I was going to do something like that then I might as well do it myself.

If you want to see the quality of things that I am usually involved with look at the artwork for one of my events that I run called Daybreaker: http://www.daybreaker.example/daybreaker-festival-anthems-ft-loomsparrow-harvest-night-eve-metro-report/

That will give you an idea of what type of quality things that I am involved with, so you need to be up for the task..

```html
<!DOCTYPE html>
<html lang="en">
<head>
<meta charset="utf-8">
<title>The Lantern Shop Plan — Book Cover</title>
<link rel="stylesheet" href="https://fonts.googleapis.com/css2?family=Anton&family=Archivo+Black&family=Archivo:ital,wght@1,800&family=Poppins:wght@600&display=swap">
<style>
  :root {
    --page: #ffffff;
    --charcoal: #404040;
    --lime: #d3db2b;
    --white: #ffffff;
    --dial-light: #f4f4f4;
    --dial-mid: #c9c9c9;
    --dial-edge: #8c8c8c;
  }
  * { margin: 0; padding: 0; box-sizing: border-box; }
  html, body { width: 1200px; height: 1000px; overflow: hidden; background: var(--page); }
  .cover {
    position: absolute; left: 330px; top: 74px;
    width: 592px; height: 866px;
    background: var(--charcoal);
  }
  .author-band {
    position: absolute; left: 0; top: 22px;
    width: 440px; height: 64px;
    background: linear-gradient(90deg, var(--lime) 0%, var(--lime) 45%, var(--charcoal) 100%);
  }
  .author {
    position: absolute; left: 22px; top: 9px;
    font-family: "Poppins", sans-serif; font-weight: 600;
    font-size: 33px; color: var(--white); white-space: nowrap;
  }
  .title {
    position: absolute; left: 2px; top: 208px;
    width: 586px; height: 220px; overflow: visible;
  }
  .title text {
    font-family: "Anton", sans-serif; fill: var(--lime);
    font-size: 112px;
  }
  .tagline-band {
    position: absolute; left: 140px; top: 493px;
    width: 458px; height: 47px;
    background: linear-gradient(90deg, var(--lime) 0%, var(--lime) 94%, #9a9a9a 100%);
  }
  .tagline {
    position: absolute; left: 16px; top: 8px;
    font-family: "Archivo", sans-serif; font-style: italic; font-weight: 800;
    font-size: 22px; color: var(--white); white-space: nowrap; letter-spacing: -0.4px;
  }
  .timer-art {
    position: absolute; left: 420px; top: 662px;
    width: 156px; height: 156px; border-radius: 50%;
    background: radial-gradient(circle at 45% 40%, var(--dial-light) 0%, var(--dial-light) 55%, var(--dial-mid) 72%, var(--dial-edge) 100%);
  }
  .slogan {
    position: absolute; left: 6px; top: 832px;
    width: 582px; height: 30px; overflow: visible;
  }
  .slogan text {
    font-family: "Archivo Black", sans-serif; font-style: italic;
    font-size: 19px; fill: var(--white);
  }
</style>
</head>
<body>
  <main class="cover">
    <div class="author-band"><p class="author">By Dale Vortan</p></div>

    <svg class="title" viewBox="0 0 586 220" aria-label="The Lantern Shop Plan">
      <text x="0" y="92" textLength="584" lengthAdjust="spacingAndGlyphs">THE LANTERN SHOP</text>
      <text x="0" y="208" textLength="584" lengthAdjust="spacing">PLAN !</text>
    </svg>

    <div class="tagline-band"><p class="tagline">Start an Online Business in no time at all</p></div>

    <div class="timer-art" role="img" aria-label="Stopwatch illustration showing five minutes"></div>

    <svg class="slogan" viewBox="0 0 582 30" aria-label="Escape the 9 - 5 and start your own business.">
      <text x="0" y="20" textLength="580" lengthAdjust="spacing">Escape the 9 - 5 and start your own business.</text>
    </svg>
  </main>
</body>
</html>
```